Brick lantern real estate investment company needs a poster design

We would like a poster design size 18 x 24.
Poster wording -
I WANT TO BUY YOUR ( finish with logo) logo uploaded
website- www.bricklantern.example
phone # 555-817-2643 ( color red for the phone number)
we would like to see the poster on 2 different backgrounds
Yellow background
White background
horizontal

```html
<!DOCTYPE html>
<html lang="en">
<head>
<meta charset="utf-8">
<title>Brick lantern – yard sign designs</title>
<link rel="stylesheet" href="https://fonts.googleapis.com/css2?family=Fredoka:wght@600;700&family=Arimo:wght@700&display=swap">
<style>
  :root {
    --backdrop: #6e6e6e;
    --sign-red: #e8222f;
    --sign-white: #ffffff;
    --sign-yellow: #ffec00;
    --ink: #231f20;
  }
  html, body {
    margin: 0;
    padding: 0;
    width: 1200px;
    height: 543px;
    overflow: hidden;
    background: var(--backdrop);
  }
  .canvas {
    position: relative;
    width: 1200px;
    height: 543px;
    background: radial-gradient(ellipse at 50% 40%, #9a9a9a 0%, var(--backdrop) 70%);
  }
  .sign {
    position: absolute;
    top: 88px;
    width: 491px;
    height: 367px;
    box-shadow: 0 6px 14px rgba(0,0,0,0.45);
    box-sizing: border-box;
  }
  .sign--white { left: 94px; background: var(--sign-red); }
  .sign--yellow { left: 616px; background: var(--sign-yellow); }

  .panel {
    position: absolute;
    left: 12px;
    right: 12px;
    background: var(--sign-white);
  }
  .panel--top { top: 12px; height: 224px; }
  .panel--bottom { top: 302px; height: 53px; }

  .rule {
    position: absolute;
    left: 0;
    right: 0;
    height: 3px;
    background: var(--ink);
  }
  .rule--upper { top: 231px; }
  .rule--lower { top: 305px; }

  .line {
    position: absolute;
    left: 0;
    right: 0;
    text-align: center;
    line-height: 1;
    white-space: nowrap;
  }
  .headline {
    font-family: "Fredoka", sans-serif;
    font-weight: 700;
    font-size: 50px;
    letter-spacing: 0.5px;
  }
  .headline--first { top: 19px; }
  .headline--second { top: 83px; }
  .ink { color: var(--ink); }
  .red { color: var(--sign-red); }

  .brand-name {
    top: 165px;
    font-family: "Fredoka", sans-serif;
    font-weight: 700;
    font-size: 46px;
    color: var(--ink);
  }
  .phone {
    top: 236px;
    font-family: "Arimo", sans-serif;
    font-weight: 700;
    font-size: 62px;
  }
  .sign--white .phone { color: var(--sign-white); }
  .sign--yellow .phone { color: var(--sign-red); }

  .website {
    font-size: 29px;
    color: var(--ink);
  }
  .sign--white .website {
    top: 315px;
    font-family: "Fredoka", sans-serif;
    font-weight: 600;
  }
  .sign--yellow .website {
    top: 323px;
    font-family: "Arimo", sans-serif;
    font-weight: 700;
  }
</style>
</head>
<body>
<main class="canvas">

  <section class="sign sign--white" aria-label="Yard sign on white background">
    <div class="panel panel--top"></div>
    <div class="panel panel--bottom"></div>
    <p class="line headline headline--first ink" style="margin:0">I WANT</p>
    <p class="line headline headline--second red" style="margin:0">TO BUY YOUR</p>
    <p class="line brand-name" style="margin:0">BRICK LANTERN</p>
    <p class="line phone" style="margin:0">555-817-2643</p>
    <p class="line website" style="margin:0">www.bricklantern.example</p>
  </section>

  <section class="sign sign--yellow" aria-label="Yard sign on yellow background">
    <div class="rule rule--upper"></div>
    <div class="rule rule--lower"></div>
    <p class="line headline headline--first" style="margin:0"><span class="red">I</span> <span class="ink">WANT</span></p>
    <p class="line headline headline--second" style="margin:0"><span class="ink">TO</span> <span class="red">BUY</span> <span class="ink">YOUR</span></p>
    <p class="line brand-name" style="margin:0">BRICK LANTERN</p>
    <p class="line phone" style="margin:0">555-817-2643</p>
    <p class="line website" style="margin:0">www.bricklantern.example</p>
  </section>

</main>
</body>
</html>
```